Technology Solutions Provider

Let’s design a business card that will be as simple and bold at the same time. Name, email address, website & phone number.

Target Market(s)

Small to Medium Size Business

Industry/Entity Type

It Professional

Contact Information for Business Card

Name, email, website, phone numbers

Font styles to use
Sans Serif

Colors
ec1f27
f04a50
dddddd
919191
000000
ffffff

Requirements
Must have
• Clean simple look using my existing logo. I just need to the basic contact information on this card.
Nice to have
• Im considering the square size card versus the standard size business card.
Should not have
• No Mailing Address, no list of services.

```html
<!DOCTYPE html>
<html lang="en">
<head>
<meta charset="utf-8">
<title>Vertex Systems – Business Card</title>
<link rel="stylesheet" href="https://fonts.googleapis.com/css2?family=Lato:wght@400;700&display=swap">
<style>
  :root {
    --brand-red: #ec1f27;
    --soft-red: #f04a50;
    --light-grey: #dddddd;
    --mid-grey: #919191;
    --ink: #000000;
    --paper: #ffffff;
    --backdrop: #3a3a3a;
  }
  * { box-sizing: border-box; margin: 0; padding: 0; }
  html, body {
    width: 1200px;
    height: 900px;
    overflow: hidden;
    background: var(--backdrop);
    font-family: "Lato", sans-serif;
  }
  .sheet {
    width: 1200px;
    height: 900px;
    display: flex;
    align-items: center;
    justify-content: center;
    gap: 60px;
  }
  .card {
    position: relative;
    width: 520px;
    height: 300px;
    background: var(--paper);
    overflow: hidden;
    box-shadow: 0 10px 30px rgba(0,0,0,0.45);
  }
  .brand-name {
    position: absolute;
    font-weight: 400;
    color: var(--brand-red);
    letter-spacing: 0.5px;
    white-space: nowrap;
  }
  /* front */
  .card--front .brand-name {
    top: 34px;
    left: 0;
    right: 0;
    text-align: center;
    font-size: 38px;
  }
  .divider {
    position: absolute;
    left: 70px;
    width: 395px;
    top: 138px;
    height: 1px;
    background: var(--brand-red);
  }
  .holder {
    position: absolute;
    right: 56px;
    top: 0;
    text-align: right;
  }
  .holder__name {
    position: absolute;
    right: 0;
    top: 104px;
    font-weight: 700;
    font-size: 25px;
    color: var(--brand-red);
    white-space: nowrap;
  }
  .holder__role {
    position: absolute;
    right: 0;
    top: 144px;
    font-size: 16px;
    color: var(--ink);
  }
  .contact {
    position: absolute;
    left: 26px;
    top: 150px;
    list-style: none;
    font-size: 15px;
    color: var(--ink);
  }
  .contact__item {
    display: flex;
    align-items: center;
    gap: 8px;
    line-height: 22px;
  }
  .contact__icon { width: 11px; height: 11px; flex: none; }
  .swoosh {
    position: absolute;
    left: 0;
    top: 0;
    width: 520px;
    height: 300px;
  }
  .card--front .website {
    position: absolute;
    left: 26px;
    bottom: 12px;
    font-size: 16px;
    color: var(--paper);
  }
  /* back */
  .card--back .brand-name {
    top: 100px;
    left: 0;
    right: 0;
    text-align: center;
    font-size: 46px;
  }
  .card--back .website {
    position: absolute;
    left: 100px;
    top: 196px;
    font-size: 16px;
    color: var(--ink);
  }
</style>
</head>
<body>
<main class="sheet">
  <section class="card card--front" aria-label="Card front">
    <svg class="swoosh" viewBox="0 0 520 300" aria-hidden="true">
      <path d="M0,210 Q180,232 360,300" fill="none" stroke="var(--mid-grey)" stroke-width="4"/>
      <path d="M0,228 Q170,250 330,300 L0,300 Z" fill="var(--brand-red)"/>
    </svg>
    <div class="brand-name">Vertex Systems</div>
    <div class="divider"></div>
    <div class="holder">
      <div class="holder__name">Daniel Harlow</div>
      <div class="holder__role">Manager</div>
    </div>
    <ul class="contact">
      <li class="contact__item">
        <svg class="contact__icon" viewBox="0 0 12 12" aria-hidden="true">
          <path d="M2.5,0.8 L4.4,0.8 L5,3.6 L3.7,4.6 Q4.8,7 7.4,8.3 L8.4,7 L11.2,7.6 L11.2,9.5 Q11.2,11.2 9.5,11.2 Q1,10.5 0.8,2.5 Q0.8,0.8 2.5,0.8 Z" fill="var(--brand-red)"/>
        </svg>
        <span>512 555 0147</span>
      </li>
      <li class="contact__item">
        <svg class="contact__icon" viewBox="0 0 12 12" aria-hidden="true">
          <rect x="0.5" y="2" width="11" height="8" fill="var(--brand-red)"/>
          <path d="M0.5,2 L6,6.5 L11.5,2" fill="none" stroke="var(--paper)" stroke-width="1"/>
        </svg>
        <span>info@vertexsystems.com</span>
      </li>
    </ul>
    <div class="website">www.vertexsystems.com</div>
  </section>

  <section class="card card--back" aria-label="Card back">
    <div class="brand-name">Vertex Systems</div>
    <div class="website">www.vertexsystems.com</div>
  </section>
</main>
</body>
</html>
```